Brochure Design to inject new life into an existing business to scale to North America

I need a brochure for an existing company that is relaunching in the Toronto area called MORvane. We help business professionals improve their professional appearance from head to toe. Our signature product is called R.U.D.A.X. We would like to have the main colours be aqua, blue, charcoal grey, no yellows or orange.

Target Market(s)

business professionals over 40 years old who want to improve their professional appearance in a business casual world , all year long

Font styles to use
Serif
Sans Serif

Colors
0493ce
33a6d7
33b8a4
f8fbef

Requirements
Must have
• Diagrams,
a natural flow
Colour balance
easy to read
aqua, blue, light green and charcoal grey for main colour
Nice to have
• boarders
impact pages
clear and attractive lines
Should not have
• yellow or orange
primary colours
short or sharp angles
black pages

```html
<!DOCTYPE html>
<html lang="en">
<head>
<meta charset="utf-8">
<title>MORvane – R.U.D.A.X. Brochure</title>
<link rel="stylesheet" href="https://fonts.googleapis.com/css2?family=Cormorant+Garamond:ital,wght@0,300;0,400;0,500;1,400&family=Lora:wght@400&family=Raleway:wght@400;500&display=swap">
<style>
:root{
  --frame:#7dc8d2;
  --sky:#86cbe6;
  --blue:#4aaedb;
  --teal:#3aa3b3;
  --pale:#dcedf6;
  --mist:#f3f5f7;
  --band:#eceff2;
  --ink:#4b5055;
  --soft:#7b8187;
  --white:#ffffff;
  --bg:#c7c9cc;
}
*{margin:0;padding:0;box-sizing:border-box}
html,body{width:1114px;height:1200px;overflow:hidden;background:var(--bg)}
.board{position:relative;width:1114px;height:1200px}
.page{position:absolute;width:248px;height:321px;background:var(--white);overflow:hidden;font-family:"Lora",serif;color:var(--ink)}
.page > *{position:absolute}
.raised{box-shadow:2px 3px 8px rgba(0,0,0,.18)}
.frame{inset:0;border:11px solid var(--frame);pointer-events:none}
.strip{background:var(--frame)}
.block{background:var(--pale)}
.heading{font-family:"Cormorant Garamond",serif;font-weight:400;color:var(--ink);line-height:1.05;white-space:nowrap}
.script{font-family:"Cormorant Garamond",serif;font-style:italic;color:var(--blue);line-height:1.2}
.body{font-size:3.6px;line-height:1.45;color:var(--soft)}
.body p + p{margin-top:3px}
.brand{display:flex;align-items:center;gap:5px}
.brand-name{font-family:"Cormorant Garamond",serif;font-weight:500;color:var(--teal);white-space:nowrap}
.brand-tag{font-family:"Raleway",sans-serif;font-size:4.5px;letter-spacing:1px;color:var(--ink);display:block;margin-top:1px}
.brand-dot{border-radius:50%;background:var(--teal);flex:none}
.title-band{background:var(--band)}
.acronym{font-family:"Cormorant Garamond",serif;font-weight:300;color:var(--ink);letter-spacing:2px;text-align:center;width:100%;line-height:1}
.subtitle{font-family:"Raleway",sans-serif;font-size:5px;color:var(--teal);text-align:center;width:100%}
.pillar{width:42px;height:90px;background:var(--sky);border-radius:9px;text-align:center;color:var(--white);padding-top:3px;overflow:hidden}
.pillar .letter{font-family:"Cormorant Garamond",serif;font-size:16px;font-weight:300;line-height:1}
.pillar .word{font-family:"Raleway",sans-serif;font-size:4px;letter-spacing:.2px;margin-top:2px;white-space:nowrap}
.pillar .note{font-family:"Raleway",sans-serif;font-size:3.6px;line-height:1.3;margin-top:4px;padding:0 4px;min-height:16px}
.pillar svg{margin-top:8px}
.pillar-notes{width:42px;font-size:3.4px;line-height:1.35;color:var(--soft)}
.pillar-notes .lead{color:var(--blue)}
.pillar-notes p + p{margin-top:3px}
.step-no{width:31px;height:31px;background:var(--sky);color:var(--white);font-family:"Cormorant Garamond",serif;font-size:15px;display:flex;align-items:center;justify-content:center}
.reason h4{font-family:"Cormorant Garamond",serif;font-weight:400;font-size:8px;color:var(--blue);line-height:1}
.reason p{font-size:3.5px;line-height:1.4;color:var(--soft);margin-top:1px}
.reason-icon{width:15px;height:15px;border:1px solid #c9cdd1;border-radius:50%}
.list{list-style:none;font-size:4px;line-height:1.95;color:var(--ink)}
.list li::before{content:"";display:inline-block;width:2px;height:2px;background:var(--blue);margin-right:5px;vertical-align:middle}
.checks li::before{width:2.5px;height:2.5px;background:none;border:.5px solid var(--blue)}
.social{display:flex;align-items:center;gap:4px;font-size:3.8px;color:var(--ink);height:9px}
.social i{display:block;width:5px;height:5px;background:var(--soft)}
</style>
</head>
<body>
<main class="board">

  <!-- Cover pair -->
  <section class="page" style="left:386px;top:41px">
    <div class="frame"></div>
    <div class="brand" style="left:36px;top:36px">
      <div><span class="brand-name" style="font-size:17px">Nora Halvick</span><span class="brand-tag" style="padding-left:50px">STYLE CONSULTANT</span></div>
      <span class="brand-dot" style="width:26px;height:26px;margin-left:12px"></span>
    </div>
    <div class="block" style="left:11px;top:81px;width:64px;height:64px"></div>
    <h2 class="heading" style="left:24px;top:88px;font-size:12.5px">The When<br>What Wear<br>How Method</h2>
    <p class="script" style="left:24px;top:212px;font-size:9px">You’re only<br>one step away<br>from looking &amp;<br>feeling amazing!</p>
  </section>

  <section class="page raised" style="left:456px;top:121px">
    <div class="strip" style="right:0;top:0;width:44px;height:6px"></div>
    <div class="strip" style="right:0;top:260px;width:8px;height:61px"></div>
    <div class="title-band" style="left:11px;top:22px;width:226px;height:42px"></div>
    <h1 class="acronym" style="left:0;top:24px;font-size:30px">R. U. D. A. X.</h1>
    <p class="subtitle" style="left:0;top:55px">Creating individual style with direction and purpose</p>
    <div class="block" style="left:15px;top:183px;width:72px;height:78px"></div>
    <div class="block" style="left:178px;top:165px;width:60px;height:55px;opacity:.6"></div>
    <div role="img" aria-label="Photo of a striped wide-leg outfit with a tan handbag" style="left:27px;top:74px;width:74px;height:74px;background:linear-gradient(90deg,#2c3a52,#d9dde3 50%,#2c3a52)"></div>
    <div role="img" aria-label="Photo of pale pink heeled sandals on a white background" style="left:119px;top:84px;width:74px;height:52px;background:linear-gradient(135deg,#fbf8f7,#e9d4cd)"></div>
    <div role="img" aria-label="Portrait photo of a woman with short platinum hair" style="left:35px;top:152px;width:75px;height:75px;background:linear-gradient(160deg,#c7c2bd,#e8e2dc)"></div>
    <div role="img" aria-label="Portrait photo of a bearded man" style="left:115px;top:162px;width:60px;height:74px;background:linear-gradient(160deg,#5a4a3f,#a89a8d)"></div>
    <div role="img" aria-label="Photo of tan ankle boots" style="left:187px;top:175px;width:41px;height:42px;background:linear-gradient(150deg,#f0eeec,#8a5234)"></div>
    <div role="img" aria-label="Photo of a lavender trouser suit on the street" style="left:137px;top:240px;width:52px;height:52px;background:linear-gradient(180deg,#9aa0ac,#b6aedc)"></div>
    <div class="brand" style="left:22px;top:278px">
      <div><span class="brand-name" style="font-size:13px">Nora Halvick</span><span class="brand-tag" style="padding-left:38px">STYLE CONSULTANT</span></div>
    </div>
  </section>

  <!-- Spread 1 -->
  <section class="page" style="left:44px;top:482px">
    <div class="frame"></div>
    <div class="brand" style="left:36px;top:36px">
      <div><span class="brand-name" style="font-size:17px">Nora Halvick</span><span class="brand-tag" style="padding-left:50px">STYLE CONSULTANT</span></div>
      <span class="brand-dot" style="width:26px;height:26px;margin-left:12px"></span>
    </div>
    <div class="block" style="left:11px;top:81px;width:64px;height:64px"></div>
    <h2 class="heading" style="left:24px;top:88px;font-size:12.5px">The When<br>What Wear<br>How Method</h2>
    <div class="body" style="left:108px;top:88px;width:114px">
      <p>This is the question posed to me more times than you can imagine. I have received countless calls over the years about an event coming up and what I should wear, whether a suit is needed or a sweater will do.</p>
      <p>The need to know how to present yourself has been around for decades. Parties, gatherings, groups and meetings all ask for an appropriate look, and the worst ever is standing out uncomfortably in a room of peers.</p>
      <p>When it comes to our image, the way we see ourselves and the way we want to be seen are rarely the same. We get stuck on the idea that there is one right outfit, when the real answer is a method.</p>
      <p>And this is where the When What Wear How method turns the most stressful situations into a simple formula, so you feel amazing from the inside out.</p>
    </div>
    <p class="script" style="left:24px;top:212px;font-size:9px">You’re only<br>one step away<br>from looking &amp;<br>feeling amazing!</p>
    <p class="body" style="left:108px;top:262px;width:114px">Nora can make prior arrangements to meet with you anywhere in the GTA.</p>
    <p style="left:108px;top:279px;font-size:5px;color:var(--soft)">nora@morvaneconsult.com</p>
    <p style="left:108px;top:287px;font-size:9px;color:var(--blue);font-family:'Raleway',sans-serif">905.555.0148</p>
  </section>

  <section class="page" style="left:292px;top:482px">
    <div class="strip" style="right:0;top:0;width:44px;height:6px"></div>
    <div class="strip" style="right:0;top:140px;width:8px;height:181px"></div>
    <div class="title-band" style="left:11px;top:22px;width:226px;height:42px"></div>
    <h1 class="acronym" style="left:0;top:24px;font-size:30px">R. U. D. A. X.</h1>
    <p class="subtitle" style="left:0;top:55px">Creating individual style with direction and purpose</p>
    <div class="block" style="left:15px;top:183px;width:72px;height:78px"></div>
    <div class="block" style="left:178px;top:165px;width:60px;height:55px;opacity:.6"></div>
    <div role="img" aria-label="Photo of a striped wide-leg outfit with a tan handbag" style="left:27px;top:74px;width:74px;height:74px;background:linear-gradient(90deg,#2c3a52,#d9dde3 50%,#2c3a52)"></div>
    <div role="img" aria-label="Photo of pale pink heeled sandals on a white background" style="left:119px;top:84px;width:74px;height:52px;background:linear-gradient(135deg,#fbf8f7,#e9d4cd)"></div>
    <div role="img" aria-label="Portrait photo of a woman with short platinum hair" style="left:35px;top:152px;width:75px;height:75px;background:linear-gradient(160deg,#c7c2bd,#e8e2dc)"></div>
    <div role="img" aria-label="Portrait photo of a bearded man" style="left:115px;top:162px;width:60px;height:74px;background:linear-gradient(160deg,#5a4a3f,#a89a8d)"></div>
    <div role="img" aria-label="Photo of tan ankle boots" style="left:187px;top:175px;width:41px;height:42px;background:linear-gradient(150deg,#f0eeec,#8a5234)"></div>
    <div role="img" aria-label="Photo of a lavender trouser suit on the street" style="left:137px;top:240px;width:52px;height:52px;background:linear-gradient(180deg,#9aa0ac,#b6aedc)"></div>
    <div class="brand" style="left:22px;top:278px">
      <div><span class="brand-name" style="font-size:13px">Nora Halvick</span><span class="brand-tag" style="padding-left:38px">STYLE CONSULTANT</span></div>
    </div>
  </section>

  <!-- Spread 2 -->
  <section class="page" style="left:563px;top:482px">
    <div class="frame" style="border-width:11px 10px 10px 12px"></div>
    <div class="block" style="left:40px;top:50px;width:70px;height:62px"></div>
    <div role="img" aria-label="Portrait photo of the consultant in a blue blouse" style="left:25px;top:69px;width:51px;height:72px;background:linear-gradient(160deg,#b9d6e8,#5fa7d3)"></div>
    <div class="brand" style="left:140px;top:50px">
      <div><span class="brand-name" style="font-size:12px">Nora Halvick</span><span class="brand-tag" style="padding-left:32px;font-size:4px">STYLE CONSULTANT</span></div>
    </div>
    <div class="body" style="left:86px;top:88px;width:135px">
      <p>Like you, style expert and corporate image consultant Nora Halvick has heard the expression business casual defined many different ways. Can you wear jeans to the office? Do I have to wear a suit jacket? Does what I wear really matter? Why does this apply at all levels of business?</p>
      <p>Nora has spent over thirty years in the beauty industry establishing herself as a successful business owner, stylist, mentor, educator and speaker. Unlike many consultants, her extensive experience in hair, make up and imaging gives her an unparalleled edge, providing a higher level of expertise to achieve a confident image head to toe.</p>
      <p>Nora has worked with both individuals and companies at all levels of business who want to understand how confidence and image go hand in hand. Regional colleges, law firms, wellness groups and financial advisors have partnered with Nora when they wanted their teams to learn the power of dressing for success, and her writing has appeared in national lifestyle magazines on the world of image consulting.</p>
      <p>To fully understand the way we are perceived, Nora has aligned herself with a network of industry experts to expand on many areas of personal and professional growth. From professional conduct to the impact of body language, Nora can provide a complete overview for today’s business world.</p>
    </div>
  </section>

  <section class="page" style="left:810px;top:482px;background:var(--mist)">
    <div class="strip" style="right:0;top:0;width:50px;height:6px"></div>
    <div class="strip" style="right:0;top:0;width:8px;height:55px"></div>
    <h1 class="acronym" style="left:0;top:38px;font-size:30px">R. U. D. A. X.</h1>
    <p class="subtitle" style="left:0;top:70px">Creating individual style with direction and purpose</p>

    <div class="pillar" style="left:9px;top:83px"><div class="letter">R</div><div class="word">ROLE</div><div class="note">Assert your level of authority</div>
      <svg width="20" height="14" viewBox="0 0 20 14" fill="none" stroke="#fff" stroke-width="1"><path d="M2 12h16M2 12 1 3l5 4 4-6 4 6 5-4-1 9"/></svg></div>
    <div class="pillar" style="left:54px;top:83px"><div class="letter">U</div><div class="word">UNDERSTAND</div><div class="note">Influences your image</div>
      <svg width="16" height="16" viewBox="0 0 16 16" fill="none" stroke="#fff" stroke-width="1"><circle cx="8" cy="8" r="7"/><circle cx="8" cy="8" r="4"/><circle cx="8" cy="8" r="1"/></svg></div>
    <div class="pillar" style="left:99px;top:83px"><div class="letter">D</div><div class="word">DRIVE</div><div class="note">Your energy field</div>
      <svg width="18" height="16" viewBox="0 0 18 16" fill="none" stroke="#fff" stroke-width="1"><circle cx="9" cy="6" r="2.2"/><path d="M5 12q4-5 8 0"/><path d="M3 3q-3 5 0 10M15 3q3 5 0 10"/></svg></div>
    <div class="pillar" style="left:144px;top:83px"><div class="letter">A</div><div class="word">AIM</div><div class="note">Empowerment</div>
      <svg width="16" height="18" viewBox="0 0 16 18" fill="none" stroke="#fff" stroke-width="1"><circle cx="8" cy="7" r="5.5"/><circle cx="8" cy="7" r="2.5"/><path d="M4.5 11 3 17l5-2 5 2-1.5-6"/></svg></div>
    <div class="pillar" style="left:189px;top:83px;width:44px"><div class="letter">X</div><div class="word">EXPANSION</div><div class="note">Gain more, spend less</div>
      <svg width="16" height="16" viewBox="0 0 16 16" fill="none" stroke="#fff" stroke-width="1"><circle cx="8" cy="8" r="7"/><path d="M8 3.5V8l3 2"/></svg></div>

    <div class="pillar-notes" style="left:9px;top:180px"><p class="lead">Learn how to stand out with:</p><p>Interactive one on one meeting</p><p>Workshop step 1 of Levels</p><p>When What Wear worksheet</p></div>
    <div class="pillar-notes" style="left:54px;top:180px"><p class="lead">Discover your personal blueprint by:</p><p>Colour, body, style analysis</p><p>Workshop step 2 of Industry</p><p>When What Wear worksheet</p></div>
    <div class="pillar-notes" style="left:99px;top:180px"><p class="lead">Create a difference when you walk in a room by:</p><p>Learning how to leverage your strengths</p><p>Use the elements of design to decode your style</p><p>Learn how to raise or lower your volume at will</p></div>
    <div class="pillar-notes" style="left:144px;top:180px"><p class="lead">Design your appearance through:</p><p>Workshop step 3 of Vibe and Colour</p><p>WWW worksheet</p><p>Video series and digital lookbook</p></div>
    <div class="pillar-notes" style="left:189px;top:180px"><p class="lead">Reap the benefits of having a strong foundation</p><p>Learn how to put outfits together quickly for any function</p><p>Workshop step 4 to put it all together</p></div>
  </section>

  <!-- Spread 3 -->
  <section class="page" style="left:44px;top:835px">
    <div role="img" aria-label="Photo of a woman in a white dress holding a clutch, city skyline behind" style="left:12px;top:14px;width:71px;height:70px;background:linear-gradient(160deg,#9aa5b1,#e3e2e0)"></div>
    <div role="img" aria-label="Portrait photo of a smiling man in a dark suit" style="left:88px;top:14px;width:71px;height:70px;background:linear-gradient(160deg,#2f3136,#8a7565)"></div>
    <div role="img" aria-label="Photo of a woven navy leather handbag" style="left:164px;top:14px;width:71px;height:70px;background:linear-gradient(160deg,#e8e6e3,#2e3a5a)"></div>
    <p style="left:24px;top:96px;width:200px;text-align:center;font-size:5px;color:var(--blue);line-height:1.3">We work with men and women over 40 years old, who want to improve their professional appearance in a business casual world, all year long</p>
    <div class="block" style="left:50px;top:160px;width:45px;height:48px"></div>
    <div role="img" aria-label="Photo of a man in a navy suit" style="left:12px;top:128px;width:71px;height:70px;background:linear-gradient(160deg,#cfd4da,#1f2a44)"></div>
    <div class="body" style="left:92px;top:130px;width:133px"><p>As you go through life building your career, growing a family and hitting milestones, when do you take time for you? I have seen many times over the years women putting themselves last in the name of responsibilities and obligations. The common answer I hear is “I’ll focus on me when the kids are grown” and while we have every intention of staying current along the way, the idea of knowing where to start becomes too overwhelming, and we fear it will take too much time and too much money.</p></div>
    <p style="left:12px;top:220px;width:80px;font-size:5px;line-height:1.25;color:var(--blue)">Have you ever noticed how uncomfortable you feel in ill fitting clothes?</p>
    <div class="body" style="left:12px;top:240px;width:83px"><p>It’s not only the physical discomfort, tugging and pulling at them, but the negative mental space it puts you in too. It has the ability to put us in a bad mood, often at the expense of our entire day.</p><p>While it sounds quick and easy to run in and grab a top here, a sweater there, the fact is the less we plan, the more we impulse shop, and the more valuable time and money we waste.</p></div>
    <div class="block" style="left:113px;top:202px;width:129px;height:96px;background:var(--mist)"></div>
    <div class="body" style="left:122px;top:207px;width:112px"><p>To stay relevant in this business casual world, full of virtual meetings and separate work environments, you need a game plan, and addressing your current style isn’t as daunting as you think. Regardless of your age or stage in life, establishing your style is the very essence of who you are. A seamless, ageless and timeless appearance draws on all of your strengths. One that helps you stop impulse shopping, picking up quick one-off items, or buying yet another black top. The secret is knowing what your own blueprint is and how to use it: the right shape for your silhouette, the best accessories and the pieces that connect it all.</p></div>
  </section>

  <section class="page" style="left:292px;top:835px">
    <div class="frame" style="border-width:14px 0 14px 14px"></div>
    <h2 class="heading" style="left:35px;top:38px;font-size:13px">3 Ways to work with us</h2>
    <div class="block" style="left:36px;top:67px;width:69px;height:59px"></div>
    <div class="step-no" style="left:29px;top:81px">1.</div>
    <div class="body" style="left:72px;top:81px;width:103px;color:var(--ink)"><p>Consultation: we provide one on one service with a strong deliverable whether it’s by virtual meetings or in person; we take great care in getting to know you.</p></div>
    <div class="block" style="left:150px;top:138px;width:88px;height:60px"></div>
    <div class="step-no" style="left:199px;top:151px">2.</div>
    <div class="body" style="left:72px;top:146px;width:106px;color:var(--ink)"><p>Partnership: we work closely with businesses to create dynamic team workshops and leadership skills for business appearance. Workshops and seminars help to establish a clear understanding of their roles and how their appearance will improve the company culture.</p></div>
    <div class="block" style="left:36px;top:211px;width:87px;height:57px"></div>
    <div class="step-no" style="left:29px;top:224px">3.</div>
    <div class="body" style="left:73px;top:221px;width:101px;color:var(--ink)"><p>Referral: nothing is as rewarding as getting a referral, and at MORvane we greatly appreciate your kindness and support by offering you an incentive program. With every referral who purchases a full R.U.D.A.X. in Style session, you will receive a complimentary service.</p></div>
  </section>

  <!-- Spread 4 -->
  <section class="page" style="left:563px;top:835px">
    <div class="block" style="left:5px;top:40px;width:40px;height:60px"></div>
    <div role="img" aria-label="Photo of a bright walk-in closet with shelves and hanging clothes" style="left:13px;top:15px;width:100px;height:90px;background:linear-gradient(160deg,#f4f2ef,#c9c0b6)"></div>
    <div class="brand" style="left:125px;top:15px">
      <div><span class="brand-name" style="font-size:12px">Nora Halvick</span><span class="brand-tag" style="padding-left:32px;font-size:4px">STYLE CONSULTANT</span></div>
    </div>
    <div class="block" style="left:125px;top:62px;width:30px;height:32px"></div>
    <h2 class="heading" style="left:128px;top:49px;font-size:13px">Why you<br>should work<br>with MORvane</h2>
    <div class="reason-icon" style="left:25px;top:118px"></div>
    <div class="reason" style="left:56px;top:116px;width:180px"><h4>Experience</h4><p>Head to toe expertise, knowledge and international training that supersedes anyone in our field.</p></div>
    <div class="reason-icon" style="left:25px;top:145px"></div>
    <div class="reason" style="left:56px;top:143px;width:180px"><h4>Time Saving</h4><p>When we know better, we do better, and nothing is more rewarding than having a clear understanding of how to show up and present our best selves, without wasting precious time creating it.</p></div>
    <div class="reason-icon" style="left:25px;top:178px"></div>
    <div class="reason" style="left:56px;top:175px;width:180px"><h4>Personal service</h4><p>Nothing is as intimidating as being open about how you feel regarding the way you look. At MORvane we make every moment count with consideration, kindness and understanding to make you feel at ease, and bring respect and trust so you know you’re in the hands of professionals.</p></div>
    <div class="reason-icon" style="left:25px;top:214px"></div>
    <div class="reason" style="left:56px;top:212px;width:180px"><h4>Testimony</h4><p>Nora’s ability to help you define your image is remarkable. Whether you’re wanting to align yourself with your company culture, or refresh your personal style, Nora will impress you. If you’re wanting that promotion, or want to stand out among your peers, give Nora a call. Best of all are the one-on-one shopping excursions.</p></div>
    <div class="block" style="left:24px;top:263px;width:206px;height:46px;background:#dcecee"></div>
    <div class="body" style="left:36px;top:267px;width:185px;color:var(--ink)"><p>Getting in touch with Nora and conducting an image consultation has changed the way I see myself, and given me the confidence to wear clothes and colours I wouldn’t have generally picked out. I now have the tools to understand what suits me, both in terms of colour and in cut, as well as some general style rules.</p></div>
    <p style="left:173px;top:302px;font-size:3.6px;color:var(--ink)">Maren, Oakville</p>
  </section>

  <section class="page" style="left:810px;top:835px">
    <div class="frame" style="border-width:12px 12px 13px 0"></div>
    <div class="block" style="left:20px;top:28px;width:20px;height:30px;background:var(--mist)"></div>
    <h2 class="heading" style="left:24px;top:28px;font-size:15px">Buy Today</h2>
    <p class="script" style="left:34px;top:48px;font-size:8.5px">Choose Us &amp;</p>
    <span class="brand-dot" style="left:190px;top:24px;width:30px;height:30px"></span>
    <ul class="list" style="left:39px;top:64px">
      <li>Change the way you view your image</li>
      <li>Effective, long term results you can use repeatedly</li>
      <li>Learn how to present yourself professionally</li>
      <li>Achieve consistency in your appearance</li>
      <li>Raise your confidence to another level</li>
    </ul>
    <p style="left:24px;top:110px;font-size:3.8px;line-height:1.4;color:var(--ink)">Yes, I would like to attend.<br>Please tick the box that best reflects you</p>
    <ul class="list checks" style="left:39px;top:124px;font-size:3.8px;line-height:2.1">
      <li>I feel like I’m outdated and fear I’m being overlooked for promotions</li>
      <li>I have regular virtual meetings and struggle with what’s presentable</li>
      <li>I tend to wear the same thing all the time</li>
      <li>I feel uncomfortable in dressing up because I don’t know what’s appropriate</li>
      <li>I struggle with being taken seriously at work</li>
    </ul>
    <div class="block" style="left:18px;top:202px;width:28px;height:30px"></div>
    <h3 class="heading" style="left:30px;top:206px;font-size:10px">Contact Details</h3>
    <p style="left:30px;top:217px;font-size:3.8px;line-height:1.4;color:var(--ink)">nora@morvaneconsult.com<br>www.morvaneconsult.com</p>
    <div style="left:28px;top:256px">
      <div class="social"><i></i>MORvane Consultant</div>
      <div class="social"><i></i>MORvane Consultant</div>
      <div class="social"><i></i>MORvane Consultant</div>
      <div class="social"><i></i>MORvane Consultant</div>
    </div>
    <div role="img" aria-label="Photo of a clothing rack in a boutique with a teal quote badge about lasting style" style="left:118px;top:192px;width:99px;height:102px;background:linear-gradient(160deg,#2f5d66,#7a4a52 60%,#d9c2b8)"></div>
  </section>

</main>
</body>
</html>
```